Computer Training in the Education sector - Letterhead

We need a new letter head to be designed for the company. We provide computer training fro the Education Sector, both primary and private tertiary providers. The colours will need to tie in with the website www.crossingtheriver.co.nz.
The company name is Crossing the River with the tag line of Computer Training for Educators.
The footer will need to have the following detail...
0508 PCS TUTOR
021 847 193
www.crossingtheriver.co.nz / training@crossingtheriver.co.nz
Updates

Thanks for the designs so far.

Some have watermarks in the background. Please don't worry about using watermarks as I will not be using a watermark in in a final design.
Regards,
Warren

Thank you for all the designs and the effort. There was some great concepts that came through.

Cheers
Warren

Industry/Entity Type

Computer

```html
<!DOCTYPE html>
<html lang="en">
<head>
<meta charset="utf-8">
<title>Crossing the River – Letterhead</title>
<link href="https://fonts.googleapis.com/css2?family=Source+Sans+3:wght@400;600&display=swap" rel="stylesheet">
<style>
  :root {
    --backdrop: #d9d9d9;
    --paper: #ffffff;
    --brand-blue: #1f6fc0;
    --brand-green: #5aaa3c;
    --brand-orange: #f39221;
    --tint-blue: rgba(127, 179, 220, 0.22);
    --tint-green: rgba(156, 203, 138, 0.28);
    --tint-orange: rgba(243, 146, 33, 0.30);
  }
  * { margin: 0; padding: 0; box-sizing: border-box; }
  html, body {
    width: 1200px;
    height: 900px;
    overflow: hidden;
    background: var(--backdrop);
    font-family: "Source Sans 3", "Myriad Pro", Arial, sans-serif;
  }
  .letterhead {
    position: absolute;
    left: 296px;
    top: 20px;
    width: 608px;
    height: 860px;
    background: var(--paper);
    box-shadow: 0 2px 10px rgba(0,0,0,0.18);
    overflow: hidden;
  }
  .header-band {
    position: absolute;
    left: 0;
    top: 80px;
    width: 608px;
    height: 120px;
    background:
      linear-gradient(180deg, rgba(255,255,255,0) 0%, rgba(255,255,255,0) 55%, var(--paper) 100%),
      linear-gradient(90deg, var(--tint-orange) 0%, var(--tint-green) 55%, var(--tint-blue) 100%);
  }
  .brand {
    position: absolute;
    left: 30px;
    top: 38px;
    display: flex;
    align-items: center;
    gap: 12px;
  }
  .brand-mark {
    width: 50px;
    height: 50px;
    border-radius: 50%;
    background: var(--brand-blue);
    flex: none;
  }
  .brand-name {
    font-size: 21px;
    font-weight: 600;
    color: var(--brand-blue);
    letter-spacing: 0.3px;
    line-height: 1;
    white-space: nowrap;
  }
  .brand-tagline {
    font-size: 13.5px;
    font-weight: 400;
    color: var(--brand-green);
    margin-top: 4px;
    white-space: nowrap;
  }
  .footer {
    position: absolute;
    left: 26px;
    right: 22px;
    bottom: 26px;
    font-size: 9.5px;
    font-weight: 600;
    line-height: 12px;
  }
  .footer-phone-free {
    color: var(--brand-green);
    display: flex;
    align-items: center;
    gap: 3px;
    white-space: nowrap;
  }
  .footer-rule {
    flex: 1;
    height: 1px;
    background: linear-gradient(90deg, var(--brand-orange), var(--brand-green) 40%, #7fb3dc);
  }
  .footer-phone-mobile { color: var(--brand-orange); }
  .footer-web { color: var(--brand-blue); white-space: nowrap; }
</style>
</head>
<body>
  <main class="letterhead">
    <div class="header-band" role="img" aria-label="Soft orange, green and blue header wave decoration"></div>

    <header class="brand">
      <span class="brand-mark"></span>
      <div class="brand-text">
        <div class="brand-name">CROSSING THE RIVER</div>
        <div class="brand-tagline">Computer Training for Educators.</div>
      </div>
    </header>

    <footer class="footer">
      <div class="footer-phone-free">0508 PCS TUTOR <span class="footer-rule"></span></div>
      <div class="footer-phone-mobile">021 847 193</div>
      <div class="footer-web">www.crossingtheriver.co.nz / training@crossingtheriver.co.nz</div>
    </footer>
  </main>
</body>
</html>
```